Brochure for Community-Based Therapy Company

Will be given out to patients, doctors, case managers. We are redesigning our marketing materials and would like a design for a brochure. We provide therapy to individuals who have been injured in car accidents or on the job. We provide occupational therapy, speech therapy and psychotherapy. We would like the brochure to utilize our corporate ID and color scheme that we are using for our other materials (see attached letterhead and logo).

Stock photos that are used should stay away from images of outpatient or hospital settings, stay away from photos with obvious disabilities (wheelchairs, learning to walk, etc), and nothing that looks like physical therapy, as we don't provide physical therapy only OT, Speech and psychotherapy. Would prefer to not have people wearing masks, as we will use this beyond the pandemic. Also, our staff wears business casual clothing so would prefer photos that the individuals are not wearing scrubs or other medical attire (lab coats, etc).

Target Market(s)

Patients, Physicians/Doctors, Case Managers

Industry/Entity Type

Healthcare

Requirements
Must have
• Prefer a booklet format but doesn't have to be 8.5 inch by 11 inch (can be a little smaller).

```html
<!DOCTYPE html>
<html lang="en">
<head>
<meta charset="utf-8">
<title>Meridian Recovery Partners Brochure</title>
<link href="https://fonts.googleapis.com/css2?family=Oswald:wght@500&family=Montserrat:wght@600;700&family=Roboto:ital,wght@0,400;0,500;0,700;1,400&display=swap" rel="stylesheet">
<style>
:root{
  --sage:#6f9a86;
  --sage-light:#8fb3a2;
  --ink:#1c1d1d;
  --charcoal:#3a3b3b;
  --mist:#e3e5e5;
  --paper:#ffffff;
  --stage:#e8e7e4;
  --text:#2d2f2f;
  --muted:#cfd4d2;
}
*{margin:0;padding:0;box-sizing:border-box}
html,body{width:800px;height:1200px;overflow:hidden;background:var(--stage)}
body{font-family:"Roboto",Arial,sans-serif;color:var(--text);position:relative}
.spread{position:absolute;left:20px;width:760px;height:540px;display:flex;box-shadow:0 6px 18px rgba(0,0,0,.12)}
.spread-outer{top:36px}
.spread-inner{top:624px}
.page{position:relative;width:380px;height:540px;background:var(--paper);overflow:hidden}
.page + .page{border-left:1px solid #eceeee}
.pad{padding:22px 22px 0}
p,li{font-size:6.6px;line-height:1.42}
.h-section{font-family:"Montserrat",Arial,sans-serif;font-weight:700;color:var(--sage);letter-spacing:1.6px;text-transform:uppercase;font-size:12px;line-height:1.15;margin-bottom:6px}
.h-sub{font-family:"Montserrat",Arial,sans-serif;font-weight:700;font-size:8.5px;letter-spacing:.8px;color:var(--ink);margin:7px 0 4px}
p + p{margin-top:5px}
.bold{font-weight:700}
.diag{display:flex;gap:14px}
.diag ul{list-style:none}
.diag li::before{content:"• "}
.funding{display:flex;gap:16px;margin-top:4px}
.fund{display:flex;align-items:center;gap:5px;font-size:6.6px;line-height:1.3;flex:1}
.tick{flex:none;width:11px;height:11px}
.contact-band{position:absolute;left:0;right:0;bottom:44px;background:var(--sage);color:#f2f6f4;padding:8px 22px;display:flex;justify-content:space-between;font-size:6.6px;line-height:1.4}
.contact-band .right{text-align:right}
.hours-band{position:absolute;left:0;right:0;bottom:26px;height:18px;background:var(--charcoal);color:#fff;font-family:"Montserrat",Arial,sans-serif;font-weight:600;font-size:6.8px;letter-spacing:.6px;display:flex;align-items:center;padding-left:22px}
.web-line{position:absolute;left:22px;right:22px;bottom:8px;font-family:"Montserrat",Arial,sans-serif;font-weight:700;color:var(--sage);font-size:9px;letter-spacing:.5px}
.web-line span{color:var(--muted);margin:0 6px}

/* cover page */
.page-cover{display:flex;flex-direction:column;background:var(--ink)}
.cover-top{position:relative;height:132px;flex:none}
.cover-top svg{position:absolute;inset:0;width:100%;height:100%}
.brand{position:absolute;left:26px;bottom:10px;display:flex;align-items:center;gap:6px;font-weight:700;font-size:11px;letter-spacing:1px;color:var(--charcoal);text-transform:uppercase}
.brand i{display:block;width:12px;height:12px;border-radius:50%;background:var(--sage)}
.cover-intro{background:var(--sage);padding:4px 22px 9px;flex:none}
.title{font-family:"Oswald",Arial,sans-serif;font-weight:500;font-size:34px;color:#fff;letter-spacing:1px;line-height:1;margin-bottom:5px}
.intro{color:#f0f5f2}
.cover-dark{flex:1;display:flex;gap:14px;padding:11px 20px 10px 22px;color:#e8eaea}
.cover-dark .col{flex:1}
.cover-dark .col-wide{flex:1.3}
.cover-dark p{color:#d9dcdb;font-size:6.3px;line-height:1.38}
.h-dark{font-family:"Montserrat",Arial,sans-serif;font-weight:700;font-size:8px;letter-spacing:1.3px;color:var(--sage-light);text-transform:uppercase;margin:0 0 3px}
.h-dark.big{font-size:8.6px;line-height:1.25;margin-top:9px}
.h-light{font-family:"Montserrat",Arial,sans-serif;font-weight:600;font-size:7.2px;line-height:1.2;color:#fff;margin:7px 0 2px}
.spacer{height:62px}

/* inner pages */
.icon-item{display:flex;gap:7px;margin-top:6px}
.icon-item svg{flex:none;width:14px;height:14px}
.icon-item p{font-weight:500}
.sub{padding-left:70px;font-size:6.6px;line-height:1.42}
.tick-list{list-style:none;margin-top:5px}
.tick-list li{display:flex;gap:6px;margin-bottom:3px}
.services{font-family:"Montserrat",Arial,sans-serif;font-weight:700;font-size:9px;letter-spacing:.5px;color:var(--ink);margin:6px 0 2px}
.italic p{font-style:italic}
.bullets{list-style:disc;padding-left:88px;margin-top:4px}
.lead-italic{font-style:italic}
</style>
</head>
<body>

<section class="spread spread-outer">
  <article class="page page-back">
    <div class="pad">
      <h2 class="h-section">Why our approach<br>to brain injury is unique</h2>
      <p>In more traditional therapy settings such as programs using outpatient models, attempts are made to simulate functional activities, combined with more structured tasks, all performed within their clinic environment. However, the inability to generalize learning has been shown to be a reoccurring difficulty for individuals with Traumatic Brain Injury and can often manifest in cognitive inflexibility, which makes carryover of their learned skills to the real world a challenge.</p>
      <p>Community-based treatment circumvents this difficulty by conducting therapy in the person's home, school, workplace, or other settings within their community, such as a grocery store or a post office. Clinicians are therefore able to witness first hand where a task is experiencing success or breaking down and can structure treatment accordingly. This allows for greater natural development of functional skills, with generalization issues no longer an obstacle toward meeting treatment goals.</p>
      <p>At Meridian Recovery Partners we are committed to helping people recover their cognitive, physical and psychosocial abilities following brain injury through intensive individual treatment which focuses on safety, skill building and increasing independence, community integration, and overall life satisfaction. Our treatment approach is two-fold, with emphasis not only on direct restoration of brain functions, but also on helping the individual learn compensatory strategies (e.g., internal mnemonics, organizational systems, self-cuing techniques) or acquire assistive devices (e.g., planners, electronic reminders). Such methods are designed to reduce the effects of real-world disability when there is enduring cognitive impairment, and are most effective when introduced within a person's own relevant environments.</p>

      <h2 class="h-section" style="margin-top:10px">Who we serve</h2>
      <p class="bold">We treat adults and adolescents with a variety of diagnoses. We service home and community locations throughout Southeast and mid-Michigan. Our therapists hold a variety of certifications and endorsements including CBIS (Certified Brain Injury Specialist), NeuroStim, and VoiceStrong.</p>

      <h3 class="h-sub">Diagnoses can include:</h3>
      <div class="diag">
        <ul>
          <li>Traumatic Brain Injury</li>
          <li>Postconcussional Syndrome</li>
          <li>Spinal Cord Injury</li>
          <li>Post-traumatic Stress Disorder</li>
          <li>Depression</li>
          <li>Anxiety</li>
          <li>Mood Disorders</li>
        </ul>
        <ul>
          <li>Visual Impairments</li>
          <li>Balance Disorders</li>
          <li>Movement Disorders</li>
          <li>Neuromuscular Pathologies</li>
          <li>Dysphagia</li>
          <li>Musculoskeletal/Orthopedic injuries<br>&nbsp;&nbsp;(ie. Spinal fractures/pathology, nerve injuries, pain)</li>
        </ul>
      </div>

      <h3 class="h-sub">Funding Sources include:</h3>
      <div class="funding">
        <div class="fund"><svg class="tick" viewBox="0 0 12 12"><circle cx="6" cy="6" r="5.2" fill="none" stroke="var(--sage)" stroke-width="1"/><path d="M3.5 6.2l1.8 1.8 3.3-3.6" fill="none" stroke="var(--sage)" stroke-width="1.1"/></svg>No-Fault<br>Auto Insurance</div>
        <div class="fund"><svg class="tick" viewBox="0 0 12 12"><circle cx="6" cy="6" r="5.2" fill="none" stroke="var(--sage)" stroke-width="1"/><path d="M3.5 6.2l1.8 1.8 3.3-3.6" fill="none" stroke="var(--sage)" stroke-width="1.1"/></svg>Workers Compensation<br>Insurance</div>
        <div class="fund"><svg class="tick" viewBox="0 0 12 12"><circle cx="6" cy="6" r="5.2" fill="none" stroke="var(--sage)" stroke-width="1"/><path d="M3.5 6.2l1.8 1.8 3.3-3.6" fill="none" stroke="var(--sage)" stroke-width="1.1"/></svg>Some Commercial Health<br>Insurance Carriers</div>
      </div>
    </div>

    <div class="contact-band">
      <div>Please contact us at 555-014-2200 or<br>e-mail us at intake@meridian-recovery.com for<br>more information on getting started</div>
      <div class="right">Fax: 555-014-2211<br>1200 Linden Park Way,<br>Suite 300, Fairview, MI 48000</div>
    </div>
    <div class="hours-band">Office Hours: Monday – Friday 9:00 am – 4:30 pm &nbsp;|&nbsp; Therapy Hours: By Appointment</div>
    <div class="web-line">intake@meridian-recovery.com<span>|</span>www.meridian-recovery.com</div>
  </article>

  <article class="page page-cover">
    <div class="cover-top">
      <svg viewBox="0 0 380 132" preserveAspectRatio="none">
        <defs>
          <linearGradient id="photoTone" x1="0" y1="0" x2="1" y2="1">
            <stop offset="0" stop-color="#6a7f99"/>
            <stop offset=".55" stop-color="#b79b7c"/>
            <stop offset="1" stop-color="#5e4c3c"/>
          </linearGradient>
        </defs>
        <rect x="0" y="0" width="380" height="132" fill="url(#photoTone)" role="img" aria-label="Photo of a woman in a knit sweater looking down at a task in a bright everyday setting"/>
        <path d="M0 92 Q190 44 380 92 L380 132 L0 132 Z" fill="var(--mist)"/>
      </svg>
      <div class="brand"><i></i>Meridian Recovery Partners</div>
    </div>

    <div class="cover-intro">
      <h1 class="title">WHO WE ARE</h1>
      <p class="intro">For over 25 years, our company has been using evidence-based principles of rehabilitation to assist patients with their recovery. We are out in the real world with patients every day, helping them to get their lives back. Our goal is to provide functional, home and community-based therapy to provide patient-centered holistic therapy with a state-of-the-art approach. Using the patient's natural environment such as their home, community or workplace allows us to attain measurable outcomes that turn even small successes into something bigger.</p>
    </div>

    <div class="cover-dark">
      <div class="col col-wide">
        <h3 class="h-dark">Vision Statement</h3>
        <p>To be a recognized leader in functional rehabilitation to individuals with a variety of diagnoses in the home and community based setting with an emphasis on goal-directed individual rehabilitation for addressing safety, skill building, independence, and cognitive and physical recovery.</p>
        <h3 class="h-dark big">Finding success in the rehabilitation process relies on certain key factors:</h3>
        <h4 class="h-light">Getting to Know You:</h4>
        <p>We do not set goals that are important to us, but rather we set goals that are important to you. We take input from you, and the people you trust like your physician, case manager or perhaps a trusted family member to identify your needs and then make a plan that is best suited for success.</p>
        <h4 class="h-light">Creating and Implementing a Customized Rehabilitation Plan:</h4>
        <p>After the evaluation protocols are completed, a system of long-term and short-term goals are developed using our team approach. This allows for therapy to be tailored to your individual needs. A plan of care is developed and implemented based on your goals and the results of the evaluation.</p>
      </div>
      <div class="col">
        <h3 class="h-dark">Mission Statement</h3>
        <p>Our mission is to provide high quality therapy that allows the people we serve to achieve an optimal level of functioning and to improve their quality of life.</p>
        <div class="spacer"></div>
        <h4 class="h-light">Comprehensive Evaluation:</h4>
        <p>We begin with an in-depth assessment with comprehensive evaluation protocols to determine your current level of functioning and how it compares to your prior level of functioning. We can then identify the areas that have been impacted and begin addressing them.</p>
        <h4 class="h-light">Focus on Accomplishments (Breaking Down Success):</h4>
        <p>In order to facilitate progress toward patient goals, our therapy is most effective with consistent therapy appointments and repetition across therapy disciplines, which maximizes carry over outside of therapy.</p>
      </div>
    </div>
  </article>
</section>

<section class="spread spread-inner">
  <article class="page page-left">
    <div class="pad">
      <h2 class="h-section">Speech Language Pathology</h2>
      <p class="bold" style="font-style:italic">Speech &amp; Language Pathologists are trained in the rehabilitation of deficits/disorders in the areas of language, articulation, voice, fluency, and dysphagia, with an underlying knowledge base of the neurological and physiologic processes affecting each. Deficits in the areas of attention, memory, information processing and executive functioning can impact all of the areas that speech and language pathologists treat, and are addressed in all treatment goals.</p>
      <h3 class="services">SERVICES INCLUDE:</h3>

      <div class="icon-item"><svg viewBox="0 0 14 14"><circle cx="7" cy="8" r="5" fill="none" stroke="var(--sage)" stroke-width="1"/><path d="M7 8V5.5M5.5 2h3" stroke="var(--sage)" stroke-width="1" fill="none"/></svg><p>Immediate and Short-Term Memory: compensatory strategies, modification of the environment for increased functional memory.</p></div>
      <div class="sub">- Attention and concentration</div>

      <div class="icon-item"><svg viewBox="0 0 14 14"><rect x="1.5" y="2.5" width="11" height="7.5" rx="1" fill="none" stroke="var(--sage)" stroke-width="1"/><path d="M4 10v2.5l2.5-2.5M3.8 5h6.4M3.8 7h4" stroke="var(--sage)" stroke-width="1" fill="none"/></svg><p>Expressive Language: ability to express ideas, verbally, or in written format, in a concise organized fashion.</p></div>
      <div class="sub">- Comprehension and Retention of Verbal and Written Language</div>

      <div class="icon-item"><svg viewBox="0 0 14 14"><rect x="1.5" y="1.5" width="11" height="11" rx="2" fill="none" stroke="var(--sage)" stroke-width="1"/><path d="M5.3 5.3a1.7 1.7 0 1 1 2.4 1.6c-.5.3-.7.6-.7 1.2M7 10v.3" stroke="var(--sage)" stroke-width="1" fill="none"/></svg><p>Information Processing: gradually increase in the length and complexity of information presented to allow the brain to take in and process more information at one time.</p></div>
      <div class="sub">- Word Retrieval and Thought Formulation for Verbal and Written Expression<br>- Pragmatic Language/Social Communication</div>

      <div class="icon-item"><svg viewBox="0 0 14 14"><path d="M11.5 7A4.5 4.5 0 1 1 7 2.5M7 2.5l-1.6-1.4M7 2.5L5.4 4" stroke="var(--sage)" stroke-width="1" fill="none"/></svg><p>Executive Functioning: The mental processes that enable individuals to plan, focus attention, retain instructions, and juggle multiple tasks successfully. Assist with planning, initiating, carrying out tasks, as well as assist with self-monitoring and awareness for carryover of strategies.</p></div>
      <div class="sub">- Articulation<br>- Dysarthria (lack of voluntary control)<br>- Dysphagia (swallowing disorders)<br>- Voice</div>

      <h2 class="h-section" style="margin-top:10px">Occupational Therapy</h2>
      <p class="lead-italic">Occupational Therapists are experts at the evaluation and analysis of an individual's abilities relative to the demands of an activity and use this perspective in order to determine any aspects of the person's life that have been impacted, including activities of daily living (i.e., self-care), instrumental activities of daily living (i.e., home management, rest and sleep habits, work demands, play, leisure, and social participation). Treatment includes re-learning how to do activities (remediation) or determining new ways of accomplishing them (compensatory strategies).</p>
      <ul class="tick-list">
        <li><svg class="tick" viewBox="0 0 12 12"><circle cx="6" cy="6" r="5.2" fill="none" stroke="var(--sage)" stroke-width="1"/><path d="M3.5 6.2l1.8 1.8 3.3-3.6" fill="none" stroke="var(--sage)" stroke-width="1.1"/></svg><span>Treatment of musculoskeletal (i.e., muscle strength, range of motion), sensory, perceptual, vestibular, and vascular, skin, or connective tissue impairments.</span></li>
        <li><svg class="tick" viewBox="0 0 12 12"><circle cx="6" cy="6" r="5.2" fill="none" stroke="var(--sage)" stroke-width="1"/><path d="M3.5 6.2l1.8 1.8 3.3-3.6" fill="none" stroke="var(--sage)" stroke-width="1.1"/></svg><span>Teach the use of memory compensation techniques such as daily planners, technological devices, checklists, and cueing systems</span></li>
        <li><svg class="tick" viewBox="0 0 12 12"><circle cx="6" cy="6" r="5.2" fill="none" stroke="var(--sage)" stroke-width="1"/><path d="M3.5 6.2l1.8 1.8 3.3-3.6" fill="none" stroke="var(--sage)" stroke-width="1.1"/></svg><span>Assist in developing effective schedules and routines</span></li>
        <li><svg class="tick" viewBox="0 0 12 12"><circle cx="6" cy="6" r="5.2" fill="none" stroke="var(--sage)" stroke-width="1"/><path d="M3.5 6.2l1.8 1.8 3.3-3.6" fill="none" stroke="var(--sage)" stroke-width="1.1"/></svg><span>Instruct individuals and family members in techniques to cope with behavioral changes and low frustration tolerance</span></li>
        <li><svg class="tick" viewBox="0 0 12 12"><circle cx="6" cy="6" r="5.2" fill="none" stroke="var(--sage)" stroke-width="1"/><path d="M3.5 6.2l1.8 1.8 3.3-3.6" fill="none" stroke="var(--sage)" stroke-width="1.1"/></svg><span>Assessment and treatment to maximize safety in the home and community environments.</span></li>
        <li><svg class="tick" viewBox="0 0 12 12"><circle cx="6" cy="6" r="5.2" fill="none" stroke="var(--sage)" stroke-width="1"/><path d="M3.5 6.2l1.8 1.8 3.3-3.6" fill="none" stroke="var(--sage)" stroke-width="1.1"/></svg><span>Recommendation of environmental adaptations to assist with physical, perceptual, and cognitive functioning, such as labeling cupboards and drawers, or using lighting to improve vision and/or attention to task</span></li>
      </ul>
    </div>
  </article>

  <article class="page page-right">
    <div class="pad">
      <ul class="tick-list" style="margin-top:0">
        <li><svg class="tick" viewBox="0 0 12 12"><circle cx="6" cy="6" r="5.2" fill="none" stroke="var(--sage)" stroke-width="1"/><path d="M3.5 6.2l1.8 1.8 3.3-3.6" fill="none" stroke="var(--sage)" stroke-width="1.1"/></svg><span>Assist in re-learning social skills through techniques such as pre-processing and rehearsal, where the individual and therapist anticipate challenging social situations and practice appropriate responses</span></li>
        <li><svg class="tick" viewBox="0 0 12 12"><circle cx="6" cy="6" r="5.2" fill="none" stroke="var(--sage)" stroke-width="1"/><path d="M3.5 6.2l1.8 1.8 3.3-3.6" fill="none" stroke="var(--sage)" stroke-width="1.1"/></svg><span>Provide cognitive retraining exercises to address specific cognitive skills, such as attention, memory, and executive functioning</span></li>
        <li><svg class="tick" viewBox="0 0 12 12"><circle cx="6" cy="6" r="5.2" fill="none" stroke="var(--sage)" stroke-width="1"/><path d="M3.5 6.2l1.8 1.8 3.3-3.6" fill="none" stroke="var(--sage)" stroke-width="1.1"/></svg><span>Provide training and adaptation for activities of daily living, such as dressing, bathing, and grooming</span></li>
        <li><svg class="tick" viewBox="0 0 12 12"><circle cx="6" cy="6" r="5.2" fill="none" stroke="var(--sage)" stroke-width="1"/><path d="M3.5 6.2l1.8 1.8 3.3-3.6" fill="none" stroke="var(--sage)" stroke-width="1.1"/></svg><span>Provide training and assist in the development of compensatory techniques for instrumental activities of daily living, such as preparing meals, shopping, managing routine financial tasks, and caring for children</span></li>
        <li><svg class="tick" viewBox="0 0 12 12"><circle cx="6" cy="6" r="5.2" fill="none" stroke="var(--sage)" stroke-width="1"/><path d="M3.5 6.2l1.8 1.8 3.3-3.6" fill="none" stroke="var(--sage)" stroke-width="1.1"/></svg><span>Assist individuals with community re-integration, working with individuals in real life settings such as the grocery store, bank, mall, workplace, home, or any other environment in which individuals need to regain competence in occupational performance.</span></li>
        <li><svg class="tick" viewBox="0 0 12 12"><circle cx="6" cy="6" r="5.2" fill="none" stroke="var(--sage)" stroke-width="1"/><path d="M3.5 6.2l1.8 1.8 3.3-3.6" fill="none" stroke="var(--sage)" stroke-width="1.1"/></svg><span>Facilitate the identification and development of healthy, meaningful hobbies or other leisure activities</span></li>
        <li><svg class="tick" viewBox="0 0 12 12"><circle cx="6" cy="6" r="5.2" fill="none" stroke="var(--sage)" stroke-width="1"/><path d="M3.5 6.2l1.8 1.8 3.3-3.6" fill="none" stroke="var(--sage)" stroke-width="1.1"/></svg><span>Consult with employers and/or educational systems to adapt the work or school environment to facilitate the individual's performance abilities</span></li>
      </ul>

      <h2 class="h-section" style="margin-top:12px">Psychological and Counseling</h2>
      <div class="italic">
        <div class="icon-item"><svg viewBox="0 0 14 14"><circle cx="5" cy="4.5" r="2" fill="none" stroke="var(--sage)" stroke-width="1"/><path d="M1.5 12a3.5 3.5 0 0 1 7 0M9.5 6.5a1.6 1.6 0 1 0 0-.1M8.5 10.5a3 3 0 0 1 4.5 1.5" fill="none" stroke="var(--sage)" stroke-width="1"/></svg><p>Individual &amp; Family<br>Counseling related to the injury</p></div>
        <div class="icon-item"><svg viewBox="0 0 14 14"><rect x="2" y="1.5" width="10" height="11" rx="1" fill="none" stroke="var(--sage)" stroke-width="1"/><path d="M4.2 4.5h5.6M4.2 7h5.6M4.2 9.5h3.6" stroke="var(--sage)" stroke-width="1"/></svg><p>Psychological services are provided<br>as needed and prescribed by the physician to:</p></div>
      </div>
      <ul class="bullets">
        <li>Address psychosocial needs of the patient.</li>
        <li>Address changes in family dynamics and other changes.</li>
        <li>Counsel the patient to ease symptoms of depression.</li>
        <li>Assist with acceptance of change of life status, as a result of the injury.</li>
        <li>Provide the individual with coping strategies.</li>
        <li>Vocational Services</li>
      </ul>

      <p class="lead-italic" style="margin-top:10px">As traditional cognitive therapy progresses and the patient is making strong progress in the areas of safety, memory, organization and other challenges, the next step is prevocational skill development or work toward a return to school or other training programs. Our occupational therapists work with patients on the following areas in order to work toward a return to work, school or training program which can include the following:</p>
      <ul class="tick-list">
        <li><svg class="tick" viewBox="0 0 12 12"><circle cx="6" cy="6" r="5.2" fill="none" stroke="var(--sage)" stroke-width="1"/><path d="M3.5 6.2l1.8 1.8 3.3-3.6" fill="none" stroke="var(--sage)" stroke-width="1.1"/></svg><span>Vocational Assessment, which includes standardized testing in order to determine the patient's aptitudes and interests in order to determine the most appropriate vocational goal/plan for the patient to be successful</span></li>
        <li><svg class="tick" viewBox="0 0 12 12"><circle cx="6" cy="6" r="5.2" fill="none" stroke="var(--sage)" stroke-width="1"/><path d="M3.5 6.2l1.8 1.8 3.3-3.6" fill="none" stroke="var(--sage)" stroke-width="1.1"/></svg><span>Vocational exploration, job development, educational options and exploration, volunteer exploration</span></li>
        <li><svg class="tick" viewBox="0 0 12 12"><circle cx="6" cy="6" r="5.2" fill="none" stroke="var(--sage)" stroke-width="1"/><path d="M3.5 6.2l1.8 1.8 3.3-3.6" fill="none" stroke="var(--sage)" stroke-width="1.1"/></svg><span>Academic support and tutoring</span></li>
        <li><svg class="tick" viewBox="0 0 12 12"><circle cx="6" cy="6" r="5.2" fill="none" stroke="var(--sage)" stroke-width="1"/><path d="M3.5 6.2l1.8 1.8 3.3-3.6" fill="none" stroke="var(--sage)" stroke-width="1.1"/></svg><span>Job analysis, job site evaluation, job coaching, job placement and shadowing</span></li>
        <li><svg class="tick" viewBox="0 0 12 12"><circle cx="6" cy="6" r="5.2" fill="none" stroke="var(--sage)" stroke-width="1"/><path d="M3.5 6.2l1.8 1.8 3.3-3.6" fill="none" stroke="var(--sage)" stroke-width="1.1"/></svg><span>Coordination with employers or school personnel to ensure adequate accommodations are in place</span></li>
      </ul>
    </div>
  </article>
</section>

</body>
</html>
```